Accounting Practice Business Card Design

I have a logo I am happy for you to use in the design of the Business Card.
You can edit and change colours as you please, I am not fixated on it.
I am looking for a modern and clean overall feel for the finished design.

The business is a small accounting practice who thrives on word of mouth referrals and this card will be given to all current and prospect clients.

Industry/Entity Type

Accountant

Contact Information for Business Card

Marcus Elwin
Level 5, 8 Corvale Ridge Road
ASHGROVE RISE VIC 3187
Phone: 9481 3057
Email: melwin@mrfaccountants.com.au
Web: www.mrfaccountants.com.au

Font styles to use
Serif
Sans Serif

Colors
0555a3
3277b5
85acd3
0393ce
33a6d7
85cae6
00a990
33b8a4
9bcb3c

Requirements
Must have
• "The end to your tax problems begin with us"
• "A referral from you is our greatest compliment"
Nice to have
• Modern clean professional

```html
<!DOCTYPE html>
<html lang="en">
<head>
<meta charset="utf-8">
<title>MRF Accountants Business Card</title>
<link href="https://fonts.googleapis.com/css2?family=Roboto:ital,wght@0,400;0,500;0,700;1,500&family=Roboto+Condensed:wght@500&display=swap" rel="stylesheet">
<style>
  :root {
    --backdrop: #2b2b2b;
    --brand-blue: #0d4176;
    --brand-green: #2e6a34;
    --paper: #f1f1f1;
    --ink-light: #ffffff;
    --card-shadow: 0 3px 8px rgba(0,0,0,0.55);
  }
  * { margin: 0; padding: 0; box-sizing: border-box; }
  html, body {
    width: 1200px; height: 960px; overflow: hidden;
    background: var(--backdrop);
    font-family: "Roboto", Arial, sans-serif;
  }
  .card {
    position: absolute;
    width: 600px; height: 343px;
    box-shadow: var(--card-shadow);
    overflow: hidden;
  }
  .card--front { left: 314px; top: 113px; background: var(--paper); }
  .card--back { left: 311px; top: 472px; background: var(--brand-blue); }

  .front-panel { position: absolute; left: 0; top: 0; width: 306px; height: 343px; }
  .front-panel-shape { position: absolute; left: 0; top: 0; }

  .holder { position: absolute; left: 42px; top: 38px; color: var(--ink-light); }
  .holder-name {
    font-family: "Roboto Condensed", "Roboto", sans-serif;
    font-weight: 500; font-size: 21px; letter-spacing: 0.2px;
    margin-bottom: 8px;
  }
  .holder-address { font-size: 14px; line-height: 19px; }

  .contact-list {
    position: absolute; right: 29px; top: 250px;
    list-style: none; color: var(--ink-light);
    font-size: 14.5px; text-align: right;
  }
  .contact-item {
    display: flex; justify-content: flex-end; align-items: center;
    height: 19px; gap: 6px; white-space: nowrap;
  }
  .contact-icon { display: block; flex: none; width: 13px; height: 13px; fill: var(--ink-light); }

  .wordmark {
    position: absolute; text-align: center;
    font-family: "Roboto", Arial, sans-serif; font-weight: 700;
    line-height: 1;
  }
  .wordmark-initials { display: block; font-size: 92px; letter-spacing: -2px; }
  .wordmark-word { display: block; font-size: 22px; letter-spacing: 0.5px; margin-top: 2px; }
  .card--front .wordmark { left: 306px; width: 294px; top: 118px; color: var(--brand-blue); }
  .card--back .wordmark { left: 0; width: 600px; top: 102px; color: var(--ink-light); }

  .taglines {
    position: absolute; left: 0; width: 600px; top: 276px;
    text-align: center; color: var(--ink-light);
    font-style: italic; font-weight: 500; font-size: 14.5px; line-height: 19px;
  }
</style>
</head>
<body>
  <section class="card card--front">
    <div class="front-panel">
      <svg class="front-panel-shape" width="306" height="343" viewBox="0 0 306 343" aria-hidden="true">
        <rect width="306" height="343" fill="var(--brand-blue)"/>
        <path d="M0 0 H306 C 295 150 160 225 0 257 Z" fill="var(--brand-green)"/>
        <path d="M0 257 C 160 225 295 150 306 0" fill="none" stroke="#ffffff" stroke-width="2.5"/>
      </svg>
      <div class="holder">
        <p class="holder-name">MARCUS ELWIN</p>
        <p class="holder-address">Level 5, 8 Corvale Ridge Road<br>ASHGROVE RISE VIC 3187</p>
      </div>
      <ul class="contact-list">
        <li class="contact-item">9481 3057
          <svg class="contact-icon" viewBox="0 0 24 24" aria-hidden="true"><path d="M6.6 10.8a15.1 15.1 0 0 0 6.6 6.6l2.2-2.2a1 1 0 0 1 1-.25 11.4 11.4 0 0 0 3.6.57 1 1 0 0 1 1 1V20a1 1 0 0 1-1 1A17 17 0 0 1 3 4a1 1 0 0 1 1-1h3.5a1 1 0 0 1 1 1c0 1.25.2 2.45.57 3.57a1 1 0 0 1-.25 1z"/></svg>
        </li>
        <li class="contact-item">melwin@mrfaccountants.com.au
          <svg class="contact-icon" viewBox="0 0 24 24" aria-hidden="true"><path d="M1 4h22v2.5l-11 6.5L1 6.5z"/><path d="M1 9l11 6.5L23 9v11H1z"/></svg>
        </li>
        <li class="contact-item">www.mrfaccountants.com.au
          <svg class="contact-icon" viewBox="0 0 24 24" aria-hidden="true"><circle cx="12" cy="12" r="11"/><path d="M7 6c2 0 3 1 3 3s-2 2-2 4 1 3 1 5M15 4c-1 2 0 3 2 3s3 2 2 4-2 3-3 5" stroke="var(--brand-blue)" stroke-width="2.2" fill="none"/></svg>
        </li>
      </ul>
    </div>
    <div class="wordmark">
      <span class="wordmark-initials">MRF</span>
      <span class="wordmark-word">ACCOUNTANTS</span>
    </div>
  </section>

  <section class="card card--back">
    <div class="wordmark">
      <span class="wordmark-initials">MRF</span>
      <span class="wordmark-word">ACCOUNTANTS</span>
    </div>
    <p class="taglines">The end to your tax problems begin with us<br>A referral from you is our greatest compliment</p>
  </section>
</body>
</html>
```